Logistics Website Design

See website https://tvarfreightglobal.com for theme and color details. Need the site to be re-done and reflect some of the designs shown in this list here: https://pinvora.com/tags/logistics-company-website

Target Market(s)

Logistics & Transportation

Industry/Entity Type

Logistics and Supply Chain

Coding

Coded - Design and coding required

Number of Pages Required

5+ page

Requirements
Must have
• Colors must match theme of logo. Looking for a sleek, interactive design.

```html
<!DOCTYPE html>
<html lang="en">
<head>
<meta charset="utf-8">
<title>Tvar Freight Global — Logistics</title>
<link rel="stylesheet" href="https://fonts.googleapis.com/css2?family=Oswald:wght@400;500;600;700&family=Roboto:wght@400;500&display=swap">
<style>
:root{
  --bg:#190c06;
  --bg-2:#24120a;
  --panel:#2c160c;
  --accent:#e8602c;
  --accent-2:#f07a45;
  --text:#f4e7dd;
  --muted:#c9b2a3;
  --line:#4a2a1b;
}
*{box-sizing:border-box;margin:0;padding:0}
html,body{width:1200px;height:5051px;overflow:hidden;background:var(--bg);color:var(--text);font-family:"Roboto",Arial,sans-serif}
.page{position:relative;width:1200px;height:5051px;overflow:hidden;background:var(--bg)}
.abs{position:absolute}
.head{font-family:"Oswald","Arial Narrow",sans-serif;font-weight:600;text-transform:uppercase;letter-spacing:-.5px;color:var(--text)}
.label{font-family:"Oswald","Arial Narrow",sans-serif;font-size:13px;letter-spacing:3px;color:var(--accent);text-transform:uppercase}
.hl{background:var(--accent);color:#1a0b05;padding:0 10px;display:inline-block}
.btn{display:inline-flex;align-items:center;gap:10px;background:var(--accent);color:#fff;border-radius:22px;font-family:"Oswald",sans-serif;font-size:14px;text-transform:uppercase;padding:0 6px 0 22px;height:40px}
.btn .arr{width:28px;height:28px;border-radius:50%;border:1.5px solid #fff;display:grid;place-items:center}
/* brand */
.brand{display:flex;align-items:center;gap:8px}
.brand-dot{width:18px;height:18px;border-radius:50%;background:var(--accent)}
.brand-name{font-family:"Oswald",sans-serif;font-weight:600;font-size:18px;color:var(--text);text-transform:uppercase}
/* hero */
.hero{left:20px;top:0;width:1158px;height:676px;border-radius:0 0 28px 28px;overflow:hidden;background:linear-gradient(100deg,#1c0d07 0%,#4a2414 55%,#6b3219 100%)}
.hero-sun{left:600px;top:20px;width:720px;height:720px;border-radius:50%;background:radial-gradient(circle at 40% 40%,#e0784a,#b5532c 70%)}
.hero-truck{left:660px;top:118px;width:498px;height:540px;background:linear-gradient(160deg,#eceae8 0%,#a9a5a3 45%,#3b2b25 100%);clip-path:polygon(25% 8%,100% 0,100% 100%,5% 100%,5% 45%)}
.nav{left:0;top:0;width:1200px;height:140px}
.nav a{position:absolute;top:62px;font-family:"Oswald",sans-serif;font-size:13px;color:var(--text);text-decoration:none;text-transform:uppercase}
.hero h1{left:82px;top:208px;width:540px;font-size:56px;line-height:66px;letter-spacing:-1px}
.hero-copy{left:82px;top:372px;width:480px;border-left:2px solid var(--accent);padding-left:16px;font-size:15px;line-height:22px;color:var(--muted)}
/* stats */
.stat{display:flex;align-items:center;gap:14px}
.stat b{font-family:"Oswald",sans-serif;font-weight:500;font-size:56px;color:var(--text)}
.stat span{font-family:"Oswald",sans-serif;font-size:13px;line-height:18px;text-transform:uppercase}
.vline{width:1px;background:var(--line)}
/* services */
.svc{width:255px;height:382px;background:linear-gradient(180deg,#2a150c,#5a2815);border-bottom:2px solid var(--accent);border-radius:4px}
.svc .ph{position:absolute;left:12px;top:12px;width:231px;height:154px}
.svc h3{position:absolute;left:74px;top:188px;font-size:18px;line-height:22px;font-weight:500}
.svc .ic{position:absolute;left:24px;top:192px;width:36px;height:36px}
.svc p{position:absolute;left:24px;top:248px;width:210px;font-size:11.5px;line-height:18px;color:var(--muted)}
.svc .go{position:absolute;left:30px;top:362px;width:34px;height:34px;border-radius:50%;background:var(--accent);display:grid;place-items:center}
/* why */
.why{left:39px;top:2068px;width:1137px;height:696px;background:linear-gradient(180deg,#2a140b 0%,#5a2a16 100%)}
.ico{width:92px;height:92px;border-radius:50%;background:var(--accent);display:grid;place-items:center}
.why h4{font-size:23px;line-height:27px;font-weight:500}
.why p{font-size:12px;line-height:20px;color:var(--muted)}
/* industries */
.ind{width:192px;height:168px;background:#2a140b;border-radius:4px;text-align:center}
.ind .ic{width:58px;height:58px;border-radius:6px;background:var(--accent);margin:26px auto 0;display:grid;place-items:center}
.ind h5{font-family:"Oswald",sans-serif;font-weight:500;font-size:16px;margin-top:26px;text-transform:uppercase}
/* testimonials */
.tst{width:322px;height:262px;border:1.5px solid #6d5448;border-radius:3px;background:#1d0e07;padding:34px 36px}
.tst p{font-size:13px;line-height:22px;color:var(--muted)}
.tst h6{font-family:"Roboto",sans-serif;font-size:15px;font-weight:500;margin-top:18px}
.stars{color:var(--accent);font-size:14px;letter-spacing:2px}
.quote-mark{position:absolute;right:14px;bottom:14px;font-family:"Oswald",sans-serif;font-size:90px;line-height:60px;color:#3b2a22}
/* footer */
.fnav a{display:flex;align-items:center;gap:18px;height:52px;border-bottom:1px solid var(--line);font-family:"Oswald",sans-serif;font-size:20px;color:var(--text);text-decoration:none;text-transform:uppercase}
.fsvc li{list-style:none;font-family:"Oswald",sans-serif;font-size:18px;height:36px;text-transform:uppercase;font-weight:400}
.fsvc li::before{content:"»";color:var(--accent);margin-right:12px}
.field{width:241px;height:35px;border:1px solid #5a3a2c;border-radius:3px;font-size:11px;color:var(--muted);display:flex;align-items:center;padding-left:14px;gap:8px}
</style>
</head>
<body>
<div class="page">

<!-- HERO -->
<section class="hero abs">
  <div class="hero-sun abs"></div>
  <div class="hero-truck abs" role="img" aria-label="White semi-truck with box trailer driving on a highway at sunset"></div>
  <h1 class="head abs">Delivering strength<br>in every mile</h1>
  <p class="hero-copy abs">We deliver a comprehensive range of open-deck and specialized transportation services—including flatbed, step deck, heavy haul, and over-dimensional freight solutions.</p>
  <a class="btn abs" style="left:82px;top:478px;height:40px">Request a quote <span class="arr"><svg width="12" height="12" viewBox="0 0 12 12"><path d="M3 9L9 3M4 3h5v5" stroke="#fff" stroke-width="1.5" fill="none"/></svg></span></a>
  <a class="btn abs" style="left:282px;top:478px;background:var(--accent);padding:0 22px 0 6px"><span class="arr" style="background:#fff;border:none"><svg width="13" height="13" viewBox="0 0 24 24"><path d="M6.6 10.8a15 15 0 006.6 6.6l2.2-2.2a1 1 0 011-.25 11 11 0 003.5.56 1 1 0 011 1V20a1 1 0 01-1 1A17 17 0 013 4a1 1 0 011-1h3.5a1 1 0 011 1c0 1.2.2 2.4.56 3.5a1 1 0 01-.25 1z" fill="#e8602c"/></svg></span>Call us now</a>
</section>

<nav class="nav abs">
  <div class="brand abs" style="left:92px;top:60px"><span class="brand-dot"></span><span class="brand-name">Tvar Freight</span></div>
  <a style="left:296px">⌂ Home</a>
  <a style="left:404px">✕ Services</a>
  <a style="left:529px">▥ Industries</a>
  <a style="left:653px">◯ About us</a>
  <a style="left:778px">☏ Contact us</a>
  <span class="btn abs" style="left:941px;top:49px;height:40px">Request a quote <span class="arr"><svg width="12" height="12" viewBox="0 0 12 12"><path d="M3 9L9 3M4 3h5v5" stroke="#fff" stroke-width="1.5" fill="none"/></svg></span></span>
</nav>

<!-- STATS -->
<div class="stat abs" style="left:102px;top:706px"><b>250</b><span>Lorem ipsum dolor sit<br>amet consectetur</span></div>
<div class="vline abs" style="left:392px;top:716px;height:56px"></div>
<div class="stat abs" style="left:476px;top:706px"><b>30K+</b><span>Lorem ipsum dolor sit<br>amet consectetur</span></div>
<div class="vline abs" style="left:808px;top:716px;height:56px"></div>
<div class="stat abs" style="left:878px;top:706px"><b>180</b><span>Lorem ipsum dolor sit<br>amet consectetur</span></div>
<div class="abs" style="left:39px;top:796px;width:1137px;height:1px;background:var(--line)"></div>

<!-- ABOUT -->
<div class="abs" style="left:30px;top:888px;width:556px;height:464px;border:3px solid var(--accent);border-left:none;border-top-color:transparent;border-radius:0 232px 232px 0"></div>
<div class="abs" role="img" aria-label="White truck with blue trailer on a motion-blurred road" style="left:37px;top:911px;width:540px;height:422px;border-radius:0 211px 211px 0;background:linear-gradient(120deg,#6b7c8e 0%,#d9d9db 40%,#8a7f78 70%,#5a3d2e 100%)"></div>
<div class="label abs" style="left:633px;top:924px">About company</div>
<h2 class="head abs" style="left:631px;top:946px;font-size:52px;line-height:66px">Keeping your supply<br><span class="hl" style="border:2px solid var(--accent)">Chain moving</span></h2>
<p class="abs" style="left:634px;top:1100px;width:500px;font-size:16px;line-height:25px;color:var(--muted)">We deliver a comprehensive range of open-deck and specialized transportation services—including flatbed, step deck, heavy haul, and over-dimensional freight solutions. Backed by years of experience, a trusted nationwide carrier network, and a strong safety-first culture, we provide reliable, adaptable logistics support built around the unique requirements of every load.</p>
<span class="btn abs" style="left:631px;top:1278px">Learn more <span class="arr"><svg width="12" height="12" viewBox="0 0 12 12"><path d="M3 9L9 3M4 3h5v5" stroke="#fff" stroke-width="1.5" fill="none"/></svg></span></span>

<!-- SERVICES -->
<div class="label abs" style="left:0;width:1200px;text-align:center;top:1444px">What we do</div>
<h2 class="head abs" style="left:0;width:1200px;text-align:center;top:1470px;font-size:52px;line-height:64px">Our <span class="hl">Services</span></h2>

<div class="svc abs" style="left:69px;top:1564px">
  <div class="ph" role="img" aria-label="Blue semi-truck hauling a trailer" style="background:linear-gradient(160deg,#a8b6c4,#4a5668 60%,#3a4a3a)"></div>
  <svg class="ic" viewBox="0 0 36 36"><rect x="4" y="14" width="28" height="6" fill="#e8602c"/><rect x="4" y="22" width="8" height="8" fill="#e8602c"/><rect x="24" y="22" width="8" height="8" fill="#e8602c"/></svg>
  <h3 class="head">Flatbed<br>Transportation</h3>
  <p>From routine shipments to oversized and heavy-haul loads, we handle freight requiring proper securement, regulatory knowledge, and consistent on-time execution.</p>
  <span class="go"><svg width="12" height="12" viewBox="0 0 12 12"><path d="M3 9L9 3M4 3h5v5" stroke="#fff" stroke-width="1.5" fill="none"/></svg></span>
</div>
<div class="svc abs" style="left:343px;top:1564px">
  <div class="ph" role="img" aria-label="Red step deck trailer parked beside a warehouse" style="background:linear-gradient(180deg,#c8cdd6,#8f8f92 55%,#a33024 80%,#5a4a44)"></div>
  <svg class="ic" viewBox="0 0 36 36"><rect x="4" y="8" width="14" height="10" fill="#e8602c"/><rect x="4" y="20" width="28" height="5" fill="#e8602c"/><circle cx="10" cy="29" r="3" fill="#e8602c"/><circle cx="26" cy="29" r="3" fill="#e8602c"/></svg>
  <h3 class="head">Step deck<br>Transportation</h3>
  <p>From routine shipments to oversized and heavy-haul loads, we handle freight requiring proper securement, regulatory knowledge, and consistent on-time execution.</p>
  <span class="go"><svg width="12" height="12" viewBox="0 0 12 12"><path d="M3 9L9 3M4 3h5v5" stroke="#fff" stroke-width="1.5" fill="none"/></svg></span>
</div>
<div class="svc abs" style="left:617px;top:1564px">
  <div class="ph" role="img" aria-label="Dry van trailers lined up at dusk" style="background:linear-gradient(180deg,#7b6a78,#c98a6a 45%,#3a3030)"></div>
  <svg class="ic" viewBox="0 0 36 36"><rect x="4" y="8" width="20" height="16" fill="none" stroke="#e8602c" stroke-width="2"/><path d="M24 14h6l3 5v5h-9z" fill="none" stroke="#e8602c" stroke-width="2"/><circle cx="10" cy="28" r="3" fill="#e8602c"/><circle cx="28" cy="28" r="3" fill="#e8602c"/></svg>
  <h3 class="head">Dry van<br>Transportation</h3>
  <p>From routine shipments to oversized and heavy-haul loads, we handle freight requiring proper securement, regulatory knowledge, and consistent on-time execution.</p>
  <span class="go"><svg width="12" height="12" viewBox="0 0 12 12"><path d="M3 9L9 3M4 3h5v5" stroke="#fff" stroke-width="1.5" fill="none"/></svg></span>
</div>
<div class="svc abs" style="left:888px;top:1564px">
  <div class="ph" role="img" aria-label="Red heavy haul truck carrying yellow machinery" style="background:linear-gradient(180deg,#9fb0c0,#c89a3a 45%,#a02a20 70%,#4a4440)"></div>
  <svg class="ic" viewBox="0 0 36 36"><rect x="3" y="10" width="20" height="14" fill="none" stroke="#fff" stroke-width="2"/><path d="M23 14h7l3 5v5H23z" fill="#fff"/><circle cx="10" cy="28" r="3" fill="#fff"/><circle cx="28" cy="28" r="3" fill="#fff"/></svg>
  <h3 class="head">Heavy haul<br>Transportation</h3>
  <p>From routine shipments to oversized and heavy-haul loads, we handle freight requiring proper securement, regulatory knowledge, and consistent on-time execution.</p>
  <span class="go"><svg width="12" height="12" viewBox="0 0 12 12"><path d="M3 9L9 3M4 3h5v5" stroke="#fff" stroke-width="1.5" fill="none"/></svg></span>
</div>

<!-- WHY CHOOSE US -->
<div class="abs" style="left:611px;top:2035px;width:1px;height:62px;background:#6d5448"></div>
<section class="why abs">
  <div class="label abs" style="left:0;width:1137px;text-align:center;top:72px">Why we are</div>
  <h2 class="head abs" style="left:0;width:1137px;text-align:center;top:96px;font-size:52px;line-height:64px">Why <span class="hl">Choose us</span></h2>
  <svg class="abs" style="left:0;top:0" width="1137" height="696" viewBox="0 0 1137 696">
    <g fill="none" stroke="#9a6a52" stroke-width="2">
      <path d="M126 300v34q0 12 12 12h340"/>
      <path d="M1021 300v34q0 12-12 12H766"/>
      <path d="M126 490v-34q0-12 12-12h340"/>
      <path d="M1021 490v-34q0-12-12-12H766"/>
    </g>
    <g fill="#3a1a0e" stroke="#e8e0da" stroke-width="2"><circle cx="126" cy="300" r="7"/><circle cx="1021" cy="300" r="7"/><circle cx="126" cy="490" r="7"/><circle cx="1021" cy="490" r="7"/></g>
    <circle cx="575" cy="382" r="148" fill="#3a1a0e" stroke="#6b3a22" stroke-width="4"/>
    <circle cx="575" cy="382" r="118" fill="none" stroke="#e8602c" stroke-width="3"/>
  </svg>
  <div class="brand abs" style="left:455px;top:366px;width:240px;justify-content:center"><span class="brand-dot"></span><span class="brand-name" style="font-size:26px">Tvar Freight</span></div>

  <div class="ico abs" style="left:80px;top:203px"><svg width="44" height="44" viewBox="0 0 44 44"><circle cx="22" cy="22" r="17" fill="none" stroke="#fff" stroke-width="3"/><path d="M22 12v11l7 4" stroke="#fff" stroke-width="3" fill="none"/></svg></div>
  <h4 class="head abs" style="left:190px;top:202px">Reliable &amp;<br>On-time delivery</h4>
  <p class="abs" style="left:192px;top:270px;width:240px">We ensure every shipment reaches its destination safely and on schedule.</p>

  <div class="ico abs" style="left:975px;top:199px"><svg width="44" height="44" viewBox="0 0 44 44"><g fill="none" stroke="#fff" stroke-width="2.5"><circle cx="22" cy="14" r="5"/><circle cx="10" cy="19" r="4"/><circle cx="34" cy="19" r="4"/><path d="M13 34a9 9 0 0118 0z"/><path d="M3 32a7 7 0 0110-6M41 32a7 7 0 00-10-6"/></g></svg></div>
  <h4 class="head abs" style="left:680px;width:291px;text-align:right;top:202px">Experienced &amp;<br>Professional team</h4>
  <p class="abs" style="left:700px;width:271px;text-align:right;top:270px">Our logistics experts bring years of industry experience to every shipment.</p>

  <div class="ico abs" style="left:80px;top:489px"><svg width="44" height="44" viewBox="0 0 44 44"><g fill="none" stroke="#fff" stroke-width="2.5"><path d="M13 6a7 7 0 017 7c0 5-7 12-7 12S6 18 6 13a7 7 0 017-7z"/><circle cx="32" cy="32" r="5"/><path d="M13 28c0 8 10 2 14 4" stroke-dasharray="3 3"/></g></svg></div>
  <h4 class="head abs" style="left:188px;top:470px">Global network<br>&amp; reach</h4>
  <p class="abs" style="left:190px;top:534px;width:260px">With a strong worldwide logistics network, we connect businesses across borders.</p>

  <div class="ico abs" style="left:975px;top:489px"><svg width="46" height="46" viewBox="0 0 46 46"><g fill="none" stroke="#fff" stroke-width="2.5"><rect x="4" y="12" width="24" height="18"/><path d="M28 17h8l6 7v6H28z"/><circle cx="12" cy="34" r="4"/><circle cx="34" cy="34" r="4"/></g></svg></div>
  <h4 class="head abs" style="left:680px;width:291px;text-align:right;top:480px">Customized<br>Logistics solutions</h4>
  <p class="abs" style="left:700px;width:271px;text-align:right;top:544px">We tailor our services to match your unique shipping and business needs.</p>
</section>

<!-- INDUSTRIES -->
<div class="abs" style="left:0;top:2800px;width:1200px;height:560px;background:radial-gradient(ellipse at 50% 60%,#3f1c0d 0%,var(--bg) 65%)"></div>
<div class="label abs" style="left:0;width:1200px;text-align:center;top:2846px">Who we serve</div>
<h2 class="head abs" style="left:0;width:1200px;text-align:center;top:2872px;font-size:52px;line-height:64px">Industries <span class="hl">We serve</span></h2>
<svg class="abs" style="left:0;top:2985px" width="1200" height="20">
  <line x1="173" y1="10" x2="1017" y2="10" stroke="#9a6a52" stroke-width="2" stroke-dasharray="3 5"/>
  <g fill="#190c06" stroke="#d8c6bb" stroke-width="2"><circle cx="173" cy="10" r="5"/><circle cx="386" cy="10" r="5"/><circle cx="594" cy="10" r="5"/><circle cx="804" cy="10" r="5"/><circle cx="1017" cy="10" r="5"/></g>
</svg>
<div class="ind abs" style="left:75px;top:3032px"><div class="ic"><svg width="32" height="32" viewBox="0 0 32 32"><path d="M4 18h24v8H4zM8 14a8 6 0 0116 0" fill="#fff"/></svg></div><h5>Food &amp; Beverage</h5></div>
<div class="ind abs" style="left:286px;top:3032px;height:192px;border:1.5px solid var(--accent);background:#2f150b">
  <div class="ic"><svg width="32" height="32" viewBox="0 0 32 32"><path d="M4 6h4l3 14h15l3-10H10" fill="none" stroke="#fff" stroke-width="2.5"/><circle cx="13" cy="26" r="2.5" fill="#fff"/><circle cx="24" cy="26" r="2.5" fill="#fff"/></svg></div>
  <h5 style="margin-top:22px">E-commerce &amp; Retail</h5>
  <p style="font-size:9.5px;line-height:14px;color:var(--muted);margin:8px 20px 0">Lorem ipsum dolor sit amet, consectetur adipiscing elit</p>
  <span class="abs" style="left:26px;top:174px;width:30px;height:30px;border-radius:50%;background:var(--accent);display:grid;place-items:center"><svg width="11" height="11" viewBox="0 0 12 12"><path d="M3 9L9 3M4 3h5v5" stroke="#fff" stroke-width="1.5" fill="none"/></svg></span>
</div>
<div class="ind abs" style="left:498px;top:3032px"><div class="ic"><svg width="32" height="32" viewBox="0 0 32 32"><circle cx="16" cy="12" r="6" fill="none" stroke="#fff" stroke-width="3"/><rect x="5" y="22" width="22" height="6" fill="#fff"/></svg></div><h5>Manufacturing</h5></div>
<div class="ind abs" style="left:708px;top:3032px"><div class="ic"><svg width="32" height="32" viewBox="0 0 32 32"><rect x="8" y="4" width="16" height="24" rx="2" fill="none" stroke="#fff" stroke-width="2.5"/><path d="M16 11v8M12 15h8" stroke="#fff" stroke-width="2.5"/></svg></div><h5>Pharma &amp; Healthcare</h5></div>
<div class="ind abs" style="left:919px;top:3032px"><div class="ic"><svg width="32" height="32" viewBox="0 0 32 32"><path d="M4 12L16 5l12 7z" fill="#fff"/><path d="M7 14v10M13 14v10M19 14v10M25 14v10" stroke="#fff" stroke-width="2.5"/><rect x="4" y="25" width="24" height="3" fill="#fff"/></svg></div><h5>Government</h5></div>

<!-- TESTIMONIALS -->
<div class="label abs" style="left:0;width:1200px;text-align:center;top:3450px">Testimonials</div>
<h2 class="head abs" style="left:0;width:1200px;text-align:center;top:3476px;font-size:52px;line-height:64px">What our <span class="hl">Client says</span></h2>
<div class="tst abs" style="left:114px;top:3583px"><p>"Lorem ipsum dolor sit amet, consectetur adipiscing elit, sed do eiusmod tempor incididunt ut labore et dolore magna aliqua. Quis ipsum suspendisse ultrices gravida. Risus commodo viverra maecenas accumsan lacus vel facilisis"</p><h6>Rena Holt</h6><div class="stars">★★★★★</div><span class="quote-mark">”</span></div>
<div class="tst abs" style="left:460px;top:3583px"><p>"Lorem ipsum dolor sit amet, consectetur adipiscing elit, sed do eiusmod tempor incididunt ut labore et dolore magna aliqua. Quis ipsum suspendisse ultrices gravida. Risus commodo viverra maecenas accumsan lacus vel facilisis"</p><h6>Rena Holt</h6><div class="stars">★★★★★</div><span class="quote-mark">”</span></div>
<div class="tst abs" style="left:808px;top:3583px"><p>"Lorem ipsum dolor sit amet, consectetur adipiscing elit, sed do eiusmod tempor incididunt ut labore et dolore magna aliqua. Quis ipsum suspendisse ultrices gravida. Risus commodo viverra maecenas accumsan lacus vel facilisis"</p><h6>Rena Holt</h6><div class="stars">★★★★★</div><span class="quote-mark">”</span></div>
<svg class="abs" style="left:520px;top:3876px" width="180" height="34" viewBox="0 0 180 34">
  <circle cx="17" cy="17" r="15" fill="#5a2a16"/><path d="M24 17H10m5-5l-5 5 5 5" stroke="#fff" stroke-width="2" fill="none"/>
  <circle cx="53" cy="17" r="3" fill="#c9b2a3"/><circle cx="76" cy="17" r="3" fill="#c9b2a3"/><circle cx="99" cy="17" r="3" fill="#c9b2a3"/><circle cx="122" cy="17" r="3" fill="#c9b2a3"/>
  <circle cx="160" cy="17" r="15" fill="none" stroke="#e8602c" stroke-width="2"/><path d="M153 17h14m-5-5l5 5-5 5" stroke="#fff" stroke-width="2" fill="none"/>
</svg>

<!-- QUOTE CTA -->
<div class="abs" style="left:20px;top:3979px;width:1156px;height:490px;border-radius:245px;background:linear-gradient(90deg,#1f0f08 0%,#4a2212 55%,#8a3d1c 100%);overflow:hidden">
  <div class="abs" role="img" aria-label="White truck cab with trailer on the road" style="left:0;top:20px;width:570px;height:450px;background:linear-gradient(110deg,#3b2a22 0%,#d8d6d4 35%,#f2f0ee 55%,#6a5a52 85%,transparent 100%);clip-path:polygon(8% 12%,60% 0,100% 30%,100% 100%,0 100%)"></div>
</div>
<div class="label abs" style="left:631px;top:4110px">Contact us</div>
<h2 class="head abs" style="left:629px;top:4138px;font-size:56px;line-height:64px">Request a <span class="hl">Quote</span></h2>
<p class="abs" style="left:631px;top:4220px;width:500px;font-size:16px;line-height:22px;color:#e6c6b4">Lorem ipsum dolor sit amet, consectetur adipiscing elit, sed do eiusmod tempor incididunt ut labore et dolore magna aliqua. Quis ipsum suspendisse ultrices gravida.</p>
<span class="btn abs" style="left:631px;top:4324px">Get in touch <span class="arr"><svg width="12" height="12" viewBox="0 0 12 12"><path d="M3 9L9 3M4 3h5v5" stroke="#fff" stroke-width="1.5" fill="none"/></svg></span></span>

<!-- FOOTER -->
<footer>
  <div class="brand abs" style="left:102px;top:4650px"><span class="brand-dot"></span><span class="brand-name" style="font-size:22px">Tvar Freight</span></div>
  <div class="abs" style="left:120px;top:4752px;display:flex;gap:16px">
    <span style="width:34px;height:34px;border-radius:50%;background:var(--accent)" role="img" aria-label="Social profile"></span>
    <span style="width:34px;height:34px;border-radius:50%;background:var(--accent)" role="img" aria-label="Social profile"></span>
    <span style="width:34px;height:34px;border-radius:50%;background:var(--accent)" role="img" aria-label="Social profile"></span>
  </div>
  <nav class="fnav abs" style="left:378px;top:4586px;width:214px">
    <a><span style="color:var(--accent)">⌂</span>Home</a>
    <a><span style="color:var(--accent)">◯</span>About</a>
    <a><span style="color:var(--accent)">▥</span>Industries</a>
    <a style="border:none"><span style="color:var(--accent)">☏</span>Contact us</a>
  </nav>
  <div class="vline abs" style="left:592px;top:4578px;height:236px"></div>
  <h3 class="head abs" style="left:637px;top:4586px;font-size:22px;font-weight:500"><span style="color:var(--accent)">✕</span> Services</h3>
  <ul class="fsvc abs" style="left:665px;top:4636px"><li>Flatbed</li><li>Step deck</li><li>Dry van</li><li>Heavy haul</li></ul>
  <div class="vline abs" style="left:837px;top:4578px;height:236px"></div>
  <h3 class="head abs" style="left:876px;top:4586px;font-size:22px;font-weight:500">Contact us</h3>
  <div class="field abs" style="left:876px;top:4635px"><span style="color:var(--accent)">●</span>Name</div>
  <div class="field abs" style="left:876px;top:4682px"><span style="color:var(--accent)">✉</span>Email address</div>
  <div class="field abs" style="left:876px;top:4729px"><span style="color:var(--accent)">☏</span>Phone</div>
  <span class="btn abs" style="left:878px;top:4778px;height:32px;font-size:11px;padding-left:14px;gap:6px">Send now <span class="arr" style="width:22px;height:22px"><svg width="10" height="10" viewBox="0 0 12 12"><path d="M3 9L9 3M4 3h5v5" stroke="#fff" stroke-width="1.5" fill="none"/></svg></span></span>
  <div class="abs" style="left:39px;top:4874px;width:1137px;height:1px;background:var(--line)"></div>
  <p class="abs" style="left:0;width:1200px;text-align:center;top:4906px;font-size:13px;color:var(--muted)">© 2026. An independent agent of Birch Haulage LLC.</p>
  <svg class="abs" style="left:1066px;top:4902px" width="20" height="20" viewBox="0 0 20 20"><path d="M3 4h14v9H8l-4 4v-4H3z" fill="#e8602c"/></svg>
  <div class="head abs" style="left:70px;top:4920px;font-size:180px;line-height:180px;font-weight:600;color:#2a1710;letter-spacing:2px;white-space:nowrap">Tvar Freight</div>
</footer>

</div>
</body>
</html>
```